Design a poster for Ellery's Dash 2023. A charity event supporting paediatric brain cancer.

We need a new poster for our event in 2023. The successful applicant will have opportunity for ongoing work with our foundation as we need a number of other deliverables once the design is finalised. We have a strong, fun and youthful brand.
Please see attached PDF showing the last 10 years of designs.
Please see attached moodboards outlining concepts for our 2023 theme. The last image of skateboarder concept is "Dusky Glow" - A retro miami vibe Juxtaposed with photo of someone from one of our previous events. Potentially posters could have multiple variants building on lots of different photos.
I have attached our brand guidelines as well as lock ups for our Ellery's Dash logos.
Whatever is created needs to be transferrable on to a number of different mediums, most importantly T-shirts, Web Banners, Billboards, Pavement Stickers, Social posts.
Our sponsor logos will remain the same.
Please only send complete designs - aligned with one of the 4 concepts provided and include all copy as per attached and include sponsors logos. Please ensure the body fonts are Brandon Grotesque and CCMatinee Idol.
Updates
Hi All, Thank you so much for all the submissions. Unfortunately after our CEO and team have reviewed the designs they are looking to go in quite a different direction than the original brief provided. I apologise for wasting your time. I have updated brief, and more specific moodboards, the last image concept is "Dusky Glow" - A retro miami vibe Juxtaposed with photo of someone from one of our previous events. Potentially posters could have multiple variants building on lots of different photos . If you would like to submit another design that would be great but if not we completely understand. Thank you again for your creative submissions.
Target Market(s)
18-35 year olds
Industry/Entity Type
Not for Profit - Fun Run Event and Party
Font styles to use
Other font styles liked:
- Fonts in Brand Guidelines - Brandon Grotesque and CCMatinee Idol
Requirements
Must have
- On Brand - colourful, focus on ALL SMILES NO MILES

```html
<!DOCTYPE html>
<html lang="en">
<head>
<meta charset="utf-8">
<title>Ellery's Dash 2023 Poster</title>
<link rel="stylesheet" href="https://fonts.googleapis.com/css2?family=Ultra&family=Montserrat:wght@500;700;900&family=Pacifico&display=swap">
<style>
  :root {
    --navy: #1f2a4d;
    --red: #e2453c;
    --blue: #3a8fcb;
    --orange: #f29b38;
    --cream: #fff6dc;
    --sun: #fde39a;
    --palm: #f6c766;
    --white: #ffffff;
  }
  * { margin: 0; padding: 0; box-sizing: border-box; }
  html, body { width: 750px; height: 1200px; overflow: hidden; background: var(--cream); }
  .poster {
    position: relative; width: 750px; height: 1200px; overflow: hidden;
    background: radial-gradient(circle at 50% 42%, #fff3c4 0, var(--sun) 45%, #fbd98a 100%);
    font-family: "Montserrat", sans-serif; color: var(--navy); text-align: center;
  }
  .palms-left, .palms-right {
    position: absolute; top: 190px; width: 230px; height: 470px;
    background: linear-gradient(180deg, rgba(246,199,102,0.85), rgba(246,199,102,0.35));
    border-radius: 48% 52% 10% 10%;
  }
  .palms-left { left: -40px; }
  .palms-right { right: -40px; }
  .cause { position: absolute; top: 34px; left: 0; right: 0; }
  .cause-lead { font-weight: 900; font-size: 26px; letter-spacing: 3px; color: var(--blue); }
  .cause-name { font-weight: 900; font-size: 52px; line-height: 1; color: var(--red); letter-spacing: 1px; }
  .stat { position: absolute; top: 140px; left: 0; right: 0; display: flex; justify-content: center; align-items: center; gap: 10px; }
  .stat-the { font-weight: 900; font-size: 22px; align-self: flex-end; margin-bottom: 10px; }
  .stat-rank { font-family: "Ultra", serif; font-size: 84px; line-height: 1; }
  .stat-text { text-align: left; font-weight: 900; line-height: 1.05; }
  .stat-text .disease { display: block; color: var(--red); font-size: 30px; }
  .stat-text .rest { display: block; font-size: 24px; }
  .title-arc { position: absolute; top: 228px; left: 0; width: 750px; height: 190px; }
  .title-arc text {
    font-family: "Ultra", serif; font-size: 112px; fill: var(--white);
    stroke: var(--navy); stroke-width: 10px; paint-order: stroke; letter-spacing: 2px;
  }
  .title-line { position: absolute; top: 400px; left: 0; right: 0; display: flex; justify-content: center; align-items: center; gap: 18px; }
  .title-date { font-weight: 900; font-size: 22px; line-height: 1.1; text-align: right; }
  .title-date .yr { color: var(--red); display: block; }
  .title-word { font-family: "Ultra", serif; font-size: 120px; line-height: 1; color: var(--navy); letter-spacing: 4px; }
  .tagline { position: absolute; top: 540px; left: 0; right: 0; font-weight: 900; font-size: 48px; letter-spacing: 1px; }
  .tagline .and { font-family: "Pacifico", cursive; font-weight: 400; color: var(--red); font-size: 36px; margin: 0 6px; }
  .event-date { position: absolute; top: 624px; left: 0; right: 0; display: flex; justify-content: center; align-items: center; gap: 14px; }
  .event-day { font-family: "Ultra", serif; font-size: 76px; color: var(--red); line-height: 1; }
  .event-day sup { font-size: 30px; vertical-align: top; }
  .event-month { display: flex; flex-direction: column; align-items: flex-start; }
  .event-weekday { background: var(--blue); color: var(--white); font-weight: 900; font-size: 18px; padding: 2px 10px; letter-spacing: 2px; }
  .event-name { font-weight: 900; font-size: 44px; letter-spacing: 1px; line-height: 1.1; }
  .anyday { position: absolute; top: 718px; left: 0; right: 0; font-weight: 700; font-size: 17px; letter-spacing: 1px; }
  .anyday .sep { color: var(--red); margin: 0 6px; }
  .register { position: absolute; top: 744px; left: 0; right: 0; font-weight: 500; font-size: 13px; }
  .foundation {
    position: absolute; top: 790px; left: 315px; width: 120px; height: 120px; border-radius: 50%;
    background: var(--navy); color: var(--white); display: flex; align-items: center; justify-content: center;
    font-weight: 900; font-size: 30px; letter-spacing: 2px;
  }
  .crowd-left, .crowd-right {
    position: absolute; top: 640px; width: 250px; height: 420px;
    background: linear-gradient(180deg, #f2a84a, #3a8fcb 60%, #1f2a4d);
    border-radius: 40% 40% 0 0; opacity: 0.9;
  }
  .crowd-left { left: 20px; }
  .crowd-right { right: 20px; }
  .sponsors {
    position: absolute; bottom: 0; left: 0; right: 0; height: 140px; background: var(--navy);
    display: flex; justify-content: space-around; align-items: center; padding: 0 30px;
  }
  .sponsor { color: var(--white); font-weight: 700; font-size: 26px; letter-spacing: 1px; }
</style>
</head>
<body>
<main class="poster">
  <div class="palms-left" role="img" aria-label="Palm tree silhouettes in pale orange"></div>
  <div class="palms-right" role="img" aria-label="Palm tree silhouettes in pale orange"></div>

  <header class="cause">
    <p class="cause-lead">SUPPORTING</p>
    <p class="cause-name">MIND FORWARD</p>
  </header>

  <div class="stat">
    <span class="stat-the">THE</span>
    <span class="stat-rank">#1</span>
    <span class="stat-text"><span class="disease">DISEASE</span><span class="rest">KILLER OF YOUNG</span></span>
  </div>

  <svg class="title-arc" viewBox="0 0 750 190" aria-label="Ellery's">
    <defs><path id="arc" d="M70 170 Q375 40 680 170"/></defs>
    <text text-anchor="middle"><textPath href="#arc" startOffset="50%">ELLERY'S</textPath></text>
  </svg>

  <div class="title-line">
    <p class="title-date">SEPT<span class="yr">2023</span></p>
    <h1 class="title-word">DASH</h1>
  </div>

  <p class="tagline">FUN RUN<span class="and">and</span>PARTY</p>

  <div class="crowd-left" role="img" aria-label="Illustrated group of cheerful runners"></div>
  <div class="crowd-right" role="img" aria-label="Illustrated pair of smiling participants"></div>

  <div class="event-date">
    <span class="event-day">10<sup>th</sup></span>
    <span class="event-month"><span class="event-weekday">SUNDAY</span><span class="event-name">SEPTEMBER</span></span>
  </div>

  <p class="anyday">YOUR WAY ANY DAY<span class="sep">|</span>ALL OF SEPTEMBER</p>
  <p class="register">Register or support a participant at ellerysdash.org</p>

  <div class="foundation">EDF</div>

  <footer class="sponsors">
    <span class="sponsor">Nimbra</span>
    <span class="sponsor">TKV</span>
    <span class="sponsor">Lumo</span>
    <span class="sponsor">Kestrel</span>
    <span class="sponsor">Harvo</span>
  </footer>
</main>
</body>
</html>
```